galactic arcade 80s vibes - jewelry company

I am looking for someone to build me a website for my jewelry company - I am going for an 80s retro GALACTIC arcade vibe. I want it to feel old school, be brightly colored (purples, greens, etc) encompass planets, stars, or milky way type vibes. My company is called LunoVix - it is zodiac signs & angel number jewelry. I want the website to open up as galaxy and my logo/name to pop up in the center of the screen and then go to the main page.

Industry/Entity Type

jewelry

Coding

Coded - Design and coding required

Number of Pages Required

1 page

Font styles to use
Other font styles liked:
• retro

Colors
0094D4
00A9DD
6FCCEA
C7EBF8
E9F6FB
00AB8E
00BBA5
67D7C9
C6EFE9
E9F9F6
59FF00
82FF00
B8FF75
E3FFCB
F4FFEA
FFF300
FFF600
FEFA6F
FFFEC7
FFFEE8
FFC000
F8CF3A
FAE287
FDF2CF
FEFAEE
E54698
E96AAD
F1A4CE
F9D9EA
FCEFF6
A7469A
B969AE
D3A5CF
EDDBEB
F8F0F9
6B429C
8869AF
B7A5CE
E3DAEB
F3F0F8

```html
<!DOCTYPE html>
<html lang="en">
<head>
<meta charset="utf-8">
<title>LunoVix — Zodiac &amp; Angel Number Jewellery</title>
<link rel="stylesheet" href="https://fonts.googleapis.com/css2?family=Audiowide&family=Poppins:wght@400;500;600;700&family=Alegreya:wght@400&family=Noto+Sans+Symbols:wght@500&display=swap">
<style>
:root{
  --space:#2b2290;
  --space-deep:#140f45;
  --footer:#1c1862;
  --green:#59ff00;
  --green-btn:#52e00a;
  --green-ink:#0d3a12;
  --magenta:#e54698;
  --violet:#a7469a;
  --purple:#6b429c;
  --white:#ffffff;
  --card-blue:#0c3f6b;
  --card-edge:#c7ebf8;
  --gold:#f8cf3a;
  --gold-deep:#c8893a;
}
*{margin:0;padding:0;box-sizing:border-box}
html,body{width:1200px;height:3122px;overflow:hidden}
body{position:relative;background:var(--space);font-family:"Poppins",sans-serif;color:var(--white)}
.abs{position:absolute}

/* hero galaxy */
.hero-sky{left:0;top:0;width:1200px;height:640px;
  background:
    radial-gradient(circle 48px at 1078px 318px,#5b8ff0 0%,#2b4fb0 55%,rgba(40,60,160,0) 100%),
    radial-gradient(circle 46px at 928px 556px,rgba(110,80,190,.9) 0%,rgba(80,60,170,.5) 70%,transparent 100%),
    radial-gradient(circle 20px at 440px 550px,rgba(110,90,200,.9),transparent 100%),
    radial-gradient(ellipse 90px 260px at 640px 150px,rgba(255,200,240,.75),transparent 75%),
    radial-gradient(ellipse 70px 200px at 560px 90px,rgba(110,220,230,.55),transparent 75%),
    radial-gradient(ellipse 160px 380px at 610px 230px,rgba(220,120,230,.6),transparent 75%),
    radial-gradient(ellipse 320px 200px at 260px 300px,rgba(150,70,220,.7),transparent 72%),
    radial-gradient(ellipse 260px 160px at 150px 120px,rgba(110,60,200,.55),transparent 72%),
    radial-gradient(ellipse 280px 240px at 940px 160px,rgba(40,40,140,.75),transparent 72%),
    radial-gradient(ellipse 400px 160px at 600px 500px,rgba(120,80,220,.5),transparent 75%),
    linear-gradient(180deg,#170f4a 0%,#2a1d7a 35%,#3a2b9c 70%,var(--space) 100%)}
.nav{top:52px;left:0;width:1200px;height:26px}
.logo{left:75px;top:-7px;font-family:"Audiowide",sans-serif;font-size:38px;color:var(--green);line-height:40px}
.nav-links{left:378px;top:0;display:flex;gap:42px;list-style:none}
.nav-links li,.foot-links li{font-family:"Audiowide",sans-serif;font-size:17px;letter-spacing:1.6px;text-transform:uppercase;line-height:26px}
.hero-title{left:0;top:222px;width:1200px;text-align:center;font-family:"Audiowide",sans-serif;font-size:106px;letter-spacing:12px;color:var(--green);line-height:120px}
.hero-sub{left:0;top:344px;width:1200px;text-align:center;font-weight:700;font-size:23px;line-height:36px;text-transform:uppercase}
.btn{display:flex;align-items:center;justify-content:center;width:172px;height:51px;background:var(--green-btn);color:var(--green-ink);font-family:"Audiowide",sans-serif;font-size:14px;letter-spacing:1px;text-transform:uppercase}

.heading{left:0;width:1200px;text-align:center;font-family:"Audiowide",sans-serif;font-size:62px;letter-spacing:5px;line-height:62px;text-transform:uppercase;
  background:linear-gradient(180deg,#f06ad0 0%,var(--violet) 55%,var(--purple) 100%);-webkit-background-clip:text;background-clip:text;color:transparent;-webkit-text-stroke:1.5px #f4c6ef}
.copy{left:160px;width:880px;text-align:center;font-size:16.5px;line-height:32.5px}

/* zodiac */
.constellations{left:0;top:1100px;width:1200px;height:620px;
  background:
    radial-gradient(ellipse 130px 160px at 80px 330px,rgba(140,210,210,.28),transparent 70%),
    radial-gradient(ellipse 110px 90px at 110px 560px,rgba(140,210,210,.25),transparent 70%),
    radial-gradient(ellipse 150px 200px at 1030px 470px,rgba(140,210,210,.3),transparent 70%),
    radial-gradient(ellipse 110px 110px at 1100px 150px,rgba(140,210,210,.22),transparent 70%),
    radial-gradient(ellipse 90px 80px at 320px 60px,rgba(140,210,210,.18),transparent 70%)}
.sign{width:146px;height:225px;border:2px solid var(--card-edge);border-radius:6px;
  background:
    radial-gradient(ellipse 46px 52px at 50% 37%,rgba(248,207,58,.95),rgba(200,137,58,.7) 55%,transparent 100%),
    radial-gradient(ellipse 30px 12px at 50% 66%,rgba(255,255,255,.35),transparent 100%),
    linear-gradient(180deg,#0f4a78,#0a3560)}
.sign .glyph{position:absolute;left:0;top:10px;width:100%;text-align:center;font-family:"Noto Sans Symbols",sans-serif;font-size:24px;line-height:28px;color:var(--white)}
.sign .label{position:absolute;left:0;bottom:12px;width:100%;text-align:center;font-family:"Alegreya",serif;font-size:22px;color:var(--gold)}

/* jewellery */
.planets{left:0;top:1840px;width:1200px;height:340px;
  background:
    radial-gradient(circle 120px at 95px 170px,#7c90c8 0%,#4a5aa0 55%,rgba(60,70,150,0) 100%),
    radial-gradient(circle 58px at 975px 80px,#b3a8d4 0%,#7a6eb0 60%,transparent 100%),
    radial-gradient(circle 28px at 1015px 200px,#4a9ae8 0%,#2a5ab0 70%,transparent 100%),
    radial-gradient(circle 40px at 380px 60px,rgba(230,150,120,.5),transparent 100%)}
.product{width:240px;height:329px;border:2px solid #c23cc0;border-radius:3px;
  background:radial-gradient(ellipse 60px 130px at 50% 45%,rgba(210,170,110,.28),transparent 100%),#fff}
.product .tag{position:absolute;left:0;bottom:14px;width:100%;text-align:center;font-family:"Alegreya",serif;font-size:20px;color:var(--gold-deep)}

/* testimonials */
.glow-band{left:0;top:2360px;width:1200px;height:560px;
  background:
    radial-gradient(ellipse 700px 120px at 600px 260px,rgba(190,90,230,.6),transparent 75%),
    linear-gradient(180deg,var(--space) 0%,#4a24a0 35%,#6a2cb0 50%,#3a1a9a 58%,#2a1a8a 72%,var(--space) 100%)}
.grid-line{left:0;top:2643px;width:1200px;height:2px;background:#a36ce8}
.avatar{left:528px;top:2503px;width:143px;height:142px;border:2px solid #c7ebf8;border-radius:4px;background:linear-gradient(180deg,#8fd0ea 0%,#78c6e6 62%,#e0632c 78%,#c94f20 100%)}
.arrow{top:2662px;width:24px;height:36px}
.name{left:0;top:2819px;width:1200px;text-align:center;font-weight:700;font-size:18px;color:var(--green)}

/* footer */
.footer{left:0;top:2919px;width:1200px;height:203px;background:var(--footer)}
.foot-links{left:0;top:57px;width:1200px;display:flex;justify-content:center;gap:55px;list-style:none}
.copyright{left:0;top:95px;width:1200px;text-align:center;font-size:14px}
.social{left:0;top:137px;width:1200px;display:flex;justify-content:center;gap:22px}
.social span{width:20px;height:20px;border-radius:50%;background:var(--white)}
</style>
</head>
<body>

<div class="abs hero-sky" role="img" aria-label="Galaxy sky with milky way, stars and planets"></div>

<header class="abs nav">
  <div class="abs logo">LunoVix</div>
  <ul class="abs nav-links">
    <li>Home</li><li>About Us</li><li>Products</li><li>Reviews</li><li>Contact Us</li>
  </ul>
</header>

<h1 class="abs hero-title">LUNOVIX</h1>
<p class="abs hero-sub">Excepteur sint occaecat cupidatat non proident<br>culpa qui officia deserunt</p>
<a class="abs btn" style="left:514px;top:442px">Read More</a>

<h2 class="abs heading" style="top:633px">Welcome to<br>LunoVix</h2>
<p class="abs copy" style="top:768px">Sed ut perspiciatis unde omnis iste natus error sit voluptatem accusantium doloremque laudantium, totam rem aperiam, eaque ipsa quae ab illo inventore veritatis et quasi architecto beatae vitae dicta sunt explicabo. Nemo enim ipsam voluptatem quia voluptas sit aspernatur aut odit aut fugit, sed quia co nsequuntur magni dolores eos qui ratione voluptatem</p>
<a class="abs btn" style="left:514px;top:925px">Read More</a>

<div class="abs constellations" role="img" aria-label="Faint constellation line drawings of zodiac creatures"></div>
<h2 class="abs heading" style="top:1082px">Zodiac Signs</h2>

<div class="abs sign" style="left:139px;top:1185px" role="img" aria-label="Aries ram illustration"><span class="glyph">♈&#xFE0E;</span><span class="label">Aries</span></div>
<div class="abs sign" style="left:295px;top:1185px" role="img" aria-label="Taurus bull illustration"><span class="glyph">♉&#xFE0E;</span><span class="label">Taurus</span></div>
<div class="abs sign" style="left:450px;top:1185px" role="img" aria-label="Gemini twins illustration"><span class="glyph">♊&#xFE0E;</span><span class="label">Gemini</span></div>
<div class="abs sign" style="left:606px;top:1185px" role="img" aria-label="Cancer crab illustration"><span class="glyph">♋&#xFE0E;</span><span class="label">Cancer</span></div>
<div class="abs sign" style="left:761px;top:1185px" role="img" aria-label="Leo lion illustration"><span class="glyph">♌&#xFE0E;</span><span class="label">Leo</span></div>
<div class="abs sign" style="left:917px;top:1185px" role="img" aria-label="Virgo maiden illustration"><span class="glyph">♍&#xFE0E;</span><span class="label">Virgo</span></div>
<div class="abs sign" style="left:295px;top:1420px" role="img" aria-label="Scorpio scorpion illustration"><span class="glyph">♏&#xFE0E;</span><span class="label">Scorpio</span></div>
<div class="abs sign" style="left:450px;top:1420px" role="img" aria-label="Sagittarius bow illustration"><span class="glyph">♐&#xFE0E;</span><span class="label">Sagittarius</span></div>
<div class="abs sign" style="left:606px;top:1420px" role="img" aria-label="Capricorn goat illustration"><span class="glyph">♑&#xFE0E;</span><span class="label">Capricorn</span></div>
<div class="abs sign" style="left:761px;top:1420px" role="img" aria-label="Aquarius water bearer illustration"><span class="glyph">♒&#xFE0E;</span><span class="label">Aquarius</span></div>

<div class="abs planets" role="img" aria-label="Earth and planets floating in space"></div>
<h2 class="abs heading" style="top:1758px;line-height:72px">Angel Number<br>Jewellery</h2>

<div class="abs product" style="left:212px;top:1954px" role="img" aria-label="Gold angel number 1999 necklace photo"><span class="tag">1999</span></div>
<div class="abs product" style="left:481px;top:1954px" role="img" aria-label="Silver angel number 1996 necklace photo"><span class="tag" style="color:#9a9aa6">1996</span></div>
<div class="abs product" style="left:751px;top:1954px" role="img" aria-label="Gold angel number 2002 necklace photo"><span class="tag">2002</span></div>

<div class="abs glow-band" role="img" aria-label="Retro neon horizon glow"></div>
<div class="abs grid-line"></div>
<h2 class="abs heading" style="top:2401px">Testimonials</h2>
<div class="abs avatar" role="img" aria-label="Customer portrait photo"></div>

<svg class="abs arrow" style="left:74px" viewBox="0 0 24 36"><polyline points="20,3 5,18 20,33" fill="none" stroke="#fff" stroke-width="2.5"/></svg>
<svg class="abs arrow" style="left:1103px" viewBox="0 0 24 36"><polyline points="4,3 19,18 4,33" fill="none" stroke="#fff" stroke-width="2.5"/></svg>

<p class="abs copy" style="top:2674px">“ Sed ut perspiciatis unde omnis iste natus error sit voluptatem accusantium doloremque laudantium, totam rem aperiam, eaque ipsa quae ab illo inventore veritatis et quasi architecto beatae vitae dicta sunt explicabo. Nemo enim ipsam voluptatem quia voluptas sit aspernatur aut odit aut fugit, sed quia co nsequuntur magni dolores eos qui ratione..”</p>
<p class="abs name">Name Heading</p>

<footer class="abs footer">
  <ul class="abs foot-links">
    <li>Home</li><li>About Us</li><li>Products</li><li>Reviews</li><li>Contact Us</li>
  </ul>
  <p class="abs copyright">Copyright ©2022 CompanyName&nbsp; All Rights Reserved.</p>
  <div class="abs social">
    <span aria-label="Social link"></span><span aria-label="Social link"></span><span aria-label="Social link"></span><span aria-label="Social link"></span><span aria-label="Social link"></span>
  </div>
</footer>

</body>
</html>
```